Pruett Design & Millwork needs a web presence. Looking for a unique Design so please submit an idea.

In brief, you should know the following about me: My company was established in 2001 and had been responsible for providing reasonable CAD Design and Custom Millwork ever since. My specialty is in the area Architectural CAD Design, Fabrication of Custom Millwork and Mouldings on a partime basis. Drawings and estimates done at a very reasonable cost. I look forward to working on your next project. Thanks in Advance, Glen 
I would like one page to show thumbnails linked to some of past millwork projects and another page with thumbnails linking to some of my house designs. I assume last page will have contact information accessed from a link on home page. I already had a logo designed which I can supply you with to design home page around. As I indicated I have a regular full time job and do this for additional income and will move to full time when I have enough business.

I have attached the logo I had designed in a couple different colors. I have also uploaded some PDF's of files that I also considered before choosing the RED LOGO to give an ideas of how we could tweak the logo to better fit the website if need be. Text is wrong in those.

Thanks,
Glen

I added my logo as a PDF side there seems to be a problem with scaling loge with the other file. Hope this helps.

Glen

Evening,
I will be hosting this site on servquill. Its looks like it will get launched with wordpress?  What will be involved from getting your design up so I can upload project pictures and and text to areas you have set aside? I am also going to upload a couple jpg of a couple recent projects so you can put in so I can get a feel of what they will look like. Thanks for all your work to date! Glen

I am not seeing alot of design variations or even many designers in fact. Is there something more from me you need? Do you need me to extend deadline?

Reason: It appears that your need some more time to submit some design changes. I will choose a design next week after changes have been submitted. Thanks for your time. Glen

Reason: Designers needs a couple days to submit some last minute changes. Thanks for all your submissions! Glen

Reason: Some last minute designs that I need to look at and give feedback on. I want to thank everyone for their designs and patience. Thanks again, Glen

Evening All,

Upon discussion with a couple of the designers I want the design done in Word Press and I have increased budget the amount they said they would need to do it for. Thanks for all submissions so far but I am still looking for the special one that stands out among the rest! Glen

I will not be extending deadline and choosing designer tomorrow morning so if you have anything else to add please do so tonight. Thanks for all your submissions. Glen

Target Market(s)

Millwork projects will be generally local where as CAD Design Projects could be emailed anywhere. Probably more USA but who knows.

Industry/Entity Type

House

Font styles to use
Other font styles liked:
• Eras Medium ITC, Calibri or Designers choice.

Requirements
Must have
• Must tie in my logo on Homepage at least. Could even be somewhat transparent in background? I will let the designer work that out.
Nice to have
• Page to point to current and past Design projects on one page and millwork on another.
Should not have
• Target a large Corporate or Global environment since it is a small business right now.

```html
<!DOCTYPE html>
<html lang="en">
<head>
<meta charset="utf-8">
<title>Pruett Design &amp; Millwork</title>
<link href="https://fonts.googleapis.com/css2?family=Arimo&family=Questrial&family=Tinos&display=swap" rel="stylesheet">
<style>
:root{
  --page:#efefef;
  --navy:#18263f;
  --ink:#222;
  --teal:#1f6a68;
  --footer:#3c3c3c;
  --footer-text:#dcdcdc;
  --tick:#23962a;
  --accent:#e08a1e;
}
*{margin:0;padding:0;box-sizing:border-box}
html,body{width:1200px;height:1148px;overflow:hidden;background:var(--page)}
.canvas{position:relative;width:1200px;height:1148px;font-family:"Arimo",sans-serif;color:var(--ink)}
.abs{position:absolute}
.header-art{left:0;top:0}
.brand-disc{left:158px;top:18px;width:174px;height:174px;border-radius:50%;background:radial-gradient(circle at 45% 40%,#dadada,#bcbcbc);display:flex;align-items:center;justify-content:center;text-align:center;font-family:"Tinos",serif;color:#2c3a46;font-size:17px;line-height:1.2}
.orb{width:86px;height:86px;border-radius:50%;box-shadow:0 5px 9px rgba(0,0,0,.45),inset 0 -6px 10px rgba(0,0,0,.6);border:2px solid #9aa3ad;overflow:hidden}
.orb::after{content:"";position:absolute;left:14px;top:5px;width:54px;height:30px;border-radius:50%;background:linear-gradient(rgba(255,255,255,.75),rgba(255,255,255,0))}
.orb-design{background:radial-gradient(circle at 50% 45%,#f07a3a 0,#b23a9a 25%,#4a3aa8 45%,#1a1d2a 75%)}
.orb-project{background:radial-gradient(circle at 50% 45%,#f0b040 0,#3fb4e8 30%,#1a6ab0 50%,#161c28 78%)}
.orb-encoding{background:radial-gradient(circle at 50% 45%,#b4e84a 0,#5aa22a 28%,#2a2f33 52%,#141618 78%)}
.orb-suite{background:radial-gradient(circle at 50% 40%,#7cc8f0 0,#2a7ab8 35%,#123050 60%,#0c1420 80%)}
.orb-label{font-family:"Tinos",serif;font-size:18px;color:#222;width:120px;text-align:center}
.navbar{left:183px;top:237px;width:836px;height:60px;border-radius:30px;background:linear-gradient(#a3a3a3,#5a5a5a);border:2px solid #d8d8d8;box-shadow:0 2px 4px rgba(0,0,0,.3)}
.nav-item{top:19px;font-family:"Tinos",serif;font-size:14px;color:#fff}
.nav-item.is-active{border-bottom:2px solid var(--accent);padding-bottom:2px}
.nav-sep{top:14px;width:1px;height:24px;background:#8a8a8a}
.search-field{left:637px;top:17px;width:130px;height:21px;border-radius:11px 0 0 11px;background:#fff}
.search-btn{left:766px;top:17px;width:34px;height:21px;background:linear-gradient(#eee,#aaa);border:1px solid #888}
.slider{left:172px;top:318px;width:856px;height:332px;border-radius:30px;background:linear-gradient(#fbfbfb,#dedede);border:1px solid #d4d4d4}
.slide-arrow{width:38px;height:38px;border-radius:50%;background:linear-gradient(#fff,#d0d0d0);border:1px solid #bbb;display:flex;align-items:center;justify-content:center;color:#999;font-size:26px;line-height:1}
.feature-title{font-family:"Tinos",serif;font-size:18px;color:var(--teal);line-height:20px;font-weight:normal}
.tick{width:26px;height:26px;border-radius:50%;background:radial-gradient(circle at 40% 35%,#4cc24c,var(--tick) 60%,#12681a);border:2px solid #fff;box-shadow:0 1px 3px rgba(0,0,0,.45)}
.feature-text{font-size:11.5px;line-height:13.6px;color:#111;white-space:nowrap}
.rule{height:1px;background:#cfcfcf}
.col-divider{width:1px;background:#cfcfcf}
.service-name{font-family:"Questrial",sans-serif;font-size:18px;color:#111}
.footer{left:0;top:933px;width:1200px;height:195px;background:var(--footer);border-top:3px solid #c9c9c9}
.footer-line{font-family:"Tinos",serif;font-size:13.5px;color:var(--footer-text);white-space:nowrap}
.tweet-box{left:791px;top:16px;width:177px;height:126px;background:#4a4a4a;border:1px solid #555}
.tweet-text{font-family:"Tinos",serif;font-size:10px;line-height:11.3px;color:#eee}
.social{width:23px;height:23px;border-radius:3px;border:1px solid #ddd;box-shadow:0 1px 2px rgba(0,0,0,.5)}
.copyright{left:0;top:1128px;width:1200px;height:20px;background:#111;color:#fff;text-align:center;font-family:"Tinos",serif;font-size:12.5px;line-height:20px}
</style>
</head>
<body>
<div class="canvas">

  <svg class="abs header-art" width="1200" height="215" viewBox="0 0 1200 215">
    <defs>
      <linearGradient id="headerShade" x1="0" y1="0" x2="0" y2="1">
        <stop offset="0" stop-color="#444"/><stop offset="1" stop-color="#6e6e6e"/>
      </linearGradient>
      <linearGradient id="officeTone" x1="0" y1="0" x2="1" y2="0">
        <stop offset="0" stop-color="#7b8893"/>
        <stop offset=".2" stop-color="#c3ccd2"/>
        <stop offset=".45" stop-color="#dfe5e8"/>
        <stop offset=".7" stop-color="#aeb8bf"/>
        <stop offset=".85" stop-color="#5d6c7c"/>
        <stop offset="1" stop-color="#4a4d52"/>
      </linearGradient>
      <linearGradient id="fadeX" x1="0" y1="0" x2="1" y2="0">
        <stop offset="0" stop-color="#fff" stop-opacity="0"/>
        <stop offset=".12" stop-color="#fff" stop-opacity="1"/>
        <stop offset=".85" stop-color="#fff" stop-opacity="1"/>
        <stop offset="1" stop-color="#fff" stop-opacity="0"/>
      </linearGradient>
      <mask id="photoFade"><rect x="320" y="14" width="690" height="200" fill="url(#fadeX)"/></mask>
      <clipPath id="waveClip"><path d="M0 0H1200V205C1100 200 1040 170 960 150C820 120 600 120 420 150C300 170 200 210 0 195Z"/></clipPath>
      <linearGradient id="waveLight" x1="0" y1="0" x2="0" y2="1">
        <stop offset="0" stop-color="#fff"/><stop offset="1" stop-color="#efefef"/>
      </linearGradient>
    </defs>
    <rect width="1200" height="215" fill="url(#waveLight)"/>
    <path d="M0 0H1200V205C1100 200 1040 170 960 150C820 120 600 120 420 150C300 170 200 210 0 195Z" fill="url(#headerShade)"/>
    <g clip-path="url(#waveClip)" mask="url(#photoFade)">
      <rect x="320" y="14" width="690" height="200" fill="url(#officeTone)" role="img" aria-label="Photo of a designer working at a desk in a bright office with city windows"/>
    </g>
    <rect x="0" y="0" width="1200" height="12" fill="var(--navy)"/>
  </svg>

  <div class="abs brand-disc"><span>PRUETT<br>Design &amp; Millwork</span></div>

  <div class="abs orb orb-design" style="left:385px;top:107px" role="img" aria-label="Glossy design icon"></div>
  <div class="abs orb orb-project" style="left:490px;top:107px" role="img" aria-label="Glossy project icon"></div>
  <div class="abs orb orb-encoding" style="left:602px;top:108px" role="img" aria-label="Glossy encoding icon"></div>
  <div class="abs orb orb-suite" style="left:722px;top:102px" role="img" aria-label="Glossy suite icon"></div>
  <div class="abs orb-label" style="left:367px;top:206px">Design</div>
  <div class="abs orb-label" style="left:473px;top:204px">Project</div>
  <div class="abs orb-label" style="left:586px;top:205px">Encoding</div>
  <div class="abs orb-label" style="left:706px;top:204px">Suite 9</div>

  <nav class="abs navbar">
    <span class="abs nav-item is-active" style="left:79px">Home</span>
    <span class="abs nav-sep" style="left:131px"></span>
    <span class="abs nav-item" style="left:146px">About</span>
    <span class="abs nav-sep" style="left:198px"></span>
    <span class="abs nav-item" style="left:213px">Portfolio</span>
    <span class="abs nav-sep" style="left:280px"></span>
    <span class="abs nav-item" style="left:293px">Download</span>
    <span class="abs nav-sep" style="left:370px"></span>
    <span class="abs nav-item" style="left:387px">Freebies</span>
    <span class="abs nav-sep" style="left:456px"></span>
    <span class="abs nav-item" style="left:474px">Contact</span>
    <span class="abs nav-sep" style="left:540px"></span>
    <span class="abs search-field"></span>
    <span class="abs search-btn">
      <svg width="32" height="19" viewBox="0 0 32 19"><circle cx="14" cy="8" r="5" fill="none" stroke="#333" stroke-width="2"/><line x1="18" y1="12" x2="22" y2="16" stroke="#333" stroke-width="2.5"/></svg>
    </span>
  </nav>

  <section class="abs slider">
    <svg class="abs" style="left:28px;top:28px" width="800" height="290" viewBox="0 0 800 290">
      <defs>
        <linearGradient id="shotA" x1="0" y1="0" x2="0" y2="1">
          <stop offset="0" stop-color="#f4f4f4"/><stop offset=".45" stop-color="#5d6f80"/><stop offset=".7" stop-color="#d8d8d8"/><stop offset=".86" stop-color="#f0f0f0"/><stop offset=".87" stop-color="#111"/><stop offset="1" stop-color="#1a1a1a"/>
        </linearGradient>
        <linearGradient id="shotB" x1="0" y1="0" x2="0" y2="1">
          <stop offset="0" stop-color="#1f9a98"/><stop offset=".08" stop-color="#1f9a98"/><stop offset=".09" stop-color="#fafafa"/><stop offset=".3" stop-color="#f0f0f0"/><stop offset=".31" stop-color="#2aa3a0"/><stop offset=".6" stop-color="#2aa3a0"/><stop offset=".61" stop-color="#e8e8e8"/><stop offset="1" stop-color="#cfcfcf"/>
        </linearGradient>
        <linearGradient id="shotC" x1="0" y1="0" x2="1" y2="1">
          <stop offset="0" stop-color="#fafafa"/><stop offset=".5" stop-color="#c9c9c9"/><stop offset="1" stop-color="#555"/>
        </linearGradient>
        <linearGradient id="shotD" x1="0" y1="0" x2="0" y2="1">
          <stop offset="0" stop-color="#3a3a3a"/><stop offset=".08" stop-color="#555"/><stop offset=".1" stop-color="#e4e4e4"/><stop offset=".5" stop-color="#f4f4f4"/><stop offset=".75" stop-color="#bdbdbd"/><stop offset="1" stop-color="#dadada"/>
        </linearGradient>
        <linearGradient id="shotE" x1="0" y1="0" x2="0" y2="1">
          <stop offset="0" stop-color="#f0f0f0"/><stop offset=".35" stop-color="#e2e2e2"/><stop offset=".4" stop-color="#5a7bbf"/><stop offset=".7" stop-color="#e8dcc0"/><stop offset="1" stop-color="#cfcfcf"/>
        </linearGradient>
        <radialGradient id="floorShadow"><stop offset="0" stop-color="#000" stop-opacity=".16"/><stop offset="1" stop-color="#000" stop-opacity="0"/></radialGradient>
      </defs>
      <ellipse cx="400" cy="252" rx="320" ry="26" fill="url(#floorShadow)"/>
      <polygon points="0,13 128,18 128,214 0,220" fill="url(#shotA)" stroke="#fff" stroke-width="3" role="img" aria-label="Website thumbnail"/>
      <polygon points="128,3 248,10 248,214 128,221" fill="url(#shotB)" stroke="#fff" stroke-width="3" role="img" aria-label="Website thumbnail"/>
      <polygon points="666,18 794,12 794,216 666,211" fill="url(#shotE)" stroke="#fff" stroke-width="3" role="img" aria-label="Website thumbnail"/>
      <polygon points="536,10 666,3 666,222 536,214" fill="url(#shotD)" stroke="#fff" stroke-width="3" role="img" aria-label="Website thumbnail"/>
      <rect x="248" y="2" width="290" height="228" fill="#fff" stroke="#e8e8e8" stroke-width="3"/>
      <rect x="251" y="5" width="284" height="222" fill="url(#shotC)" role="img" aria-label="Featured website screenshot"/>
      <rect x="251" y="174" width="284" height="50" fill="#141414"/>
      <rect x="251" y="224" width="284" height="3" fill="#b01818"/>
    </svg>
    <div class="abs slide-arrow" style="left:-14px;top:137px">&#8249;</div>
    <div class="abs slide-arrow" style="left:826px;top:137px">&#8250;</div>
  </section>

  <div class="abs col-divider" style="left:450px;top:685px;height:232px"></div>
  <div class="abs col-divider" style="left:768px;top:685px;height:232px"></div>

  <div class="abs" style="left:175px;top:700px;width:66px;height:48px;border-radius:4px;background:linear-gradient(135deg,#fafafa,#b9c2cc 55%,#6f7a86);transform:rotate(-8deg);box-shadow:1px 2px 3px rgba(0,0,0,.3)" role="img" aria-label="Font file icon"></div>
  <svg class="abs" style="left:236px;top:674px" width="26" height="26" viewBox="0 0 26 26"><circle cx="13" cy="13" r="12" fill="#23962a" stroke="#fff" stroke-width="2"/><polyline points="7,13 11,18 19,8" fill="none" stroke="#fff" stroke-width="3"/></svg>
  <h2 class="abs feature-title" style="left:269px;top:677px">Quality Fonts choice</h2>
  <div class="abs rule" style="left:256px;top:718px;width:170px"></div>
  <p class="abs feature-text" style="left:256px;top:728px">Lorem ipsum dolor sit amet<br>consectetur adipiscing elit.<br>Vestibulum eget sem sed risus<br>elementum tempor. Sed non dolor.<br>Phasellus pharetra suscipit arcu.</p>
  <div class="abs service-name" style="left:249px;top:808px">Pruett Design</div>
  <div class="abs service-name" style="left:240px;top:860px;width:110px;text-align:center;color:#555">Pruett</div>

  <div class="abs" style="left:456px;top:688px;width:74px;height:50px;border-radius:4px;background:linear-gradient(150deg,#fff,#e6e6e6 40%,#d0473a 55%,#f2f2f2 65%,#3c5ea8 90%);transform:rotate(6deg);box-shadow:1px 2px 3px rgba(0,0,0,.3)" role="img" aria-label="Documents icon"></div>
  <svg class="abs" style="left:531px;top:674px" width="26" height="26" viewBox="0 0 26 26"><circle cx="13" cy="13" r="12" fill="#23962a" stroke="#fff" stroke-width="2"/><polyline points="7,13 11,18 19,8" fill="none" stroke="#fff" stroke-width="3"/></svg>
  <h2 class="abs feature-title" style="left:568px;top:676px">Content analysis<br>and insertion</h2>
  <div class="abs rule" style="left:562px;top:719px;width:156px"></div>
  <p class="abs feature-text" style="left:563px;top:726px">Lorem ipsum dolor sit amet,<br>consectetur adipiscing elit,<br>sed do eiusmod tempor incididunt ut<br>&nbsp;labore et dolore magna aliqua.<br>Ut enim ad minim veniam,</p>
  <div class="abs service-name" style="left:563px;top:808px">CAD Design</div>
  <div class="abs" style="left:563px;top:842px;width:178px;height:62px;background:linear-gradient(160deg,#fffdf6,#efe6d2 60%,#cfc3a8);box-shadow:0 8px 12px rgba(0,0,0,.22)" role="img" aria-label="Business card sample"></div>

  <div class="abs" style="left:776px;top:674px;width:90px;height:48px;border-radius:24px;background:linear-gradient(90deg,#c81e1e,#e84a2a 30%,#3a8ad8 65%,#1d4f9a);box-shadow:1px 2px 4px rgba(0,0,0,.35)" role="img" aria-label="Browser icons"></div>
  <svg class="abs" style="left:874px;top:675px" width="26" height="26" viewBox="0 0 26 26"><circle cx="13" cy="13" r="12" fill="#23962a" stroke="#fff" stroke-width="2"/><polyline points="7,13 11,18 19,8" fill="none" stroke="#fff" stroke-width="3"/></svg>
  <h2 class="abs feature-title" style="left:907px;top:672px">Attractive Work</h2>
  <div class="abs rule" style="left:868px;top:719px;width:154px"></div>
  <p class="abs feature-text" style="left:858px;top:732px">Lorem ipsum dolor sit amet,<br>consectetur adipiscing elit,<br>sed do eiusmod tempor incidid<br>&nbsp;labore et dolore magna aliqua.<br>Ut enim ad minim veniam,</p>
  <div class="abs service-name" style="left:858px;top:812px">Custom Millwork</div>
  <div class="abs" style="left:860px;top:852px;width:140px;height:58px;background:linear-gradient(90deg,#f6f6f6,#c0392b 20%,#f2f2f2 45%,#3a3a3a 60%,#fafafa 80%,#dedede);box-shadow:0 8px 10px rgba(0,0,0,.18)" role="img" aria-label="Website shown on screens"></div>

  <footer class="abs footer">
    <span class="abs" style="left:182px;top:12px;width:20px;height:26px;border-radius:3px;background:linear-gradient(#f2c96a,#c08a2a)" role="img" aria-label="Folder icon"></span>
    <span class="abs footer-line" style="left:214px;top:22px">Were used for the design icons free</span>
    <svg class="abs" style="left:178px;top:72px" width="28" height="28" viewBox="0 0 28 28"><circle cx="14" cy="14" r="12.5" fill="#3aa63a" stroke="#fff" stroke-width="2"/><circle cx="14" cy="8" r="2" fill="#fff"/><rect x="12.2" y="11.5" width="3.6" height="10" fill="#fff"/></svg>
    <span class="abs footer-line" style="left:217px;top:87px">If you need information Contact</span>
    <span class="abs" style="left:175px;top:134px;width:30px;height:22px;border-radius:11px;background:linear-gradient(90deg,#d84a3a,#e8b040 40%,#4a7ac8 75%,#8a5ab0)" role="img" aria-label="Paint palette icon"></span>
    <span class="abs footer-line" style="left:214px;top:138px;line-height:16px">Graphics was conceived and designed<br>by the studio</span>

    <div class="abs col-divider" style="left:450px;top:14px;height:166px;background:#777"></div>
    <svg class="abs" style="left:483px;top:29px" width="14" height="22" viewBox="0 0 14 22"><rect x="1" y="1" width="12" height="20" rx="2" fill="#c9d3dc" stroke="#8899a8"/><rect x="3" y="4" width="8" height="8" fill="#5a86b0"/><circle cx="7" cy="17" r="1.5" fill="#8899a8"/></svg>
    <span class="abs footer-line" style="left:509px;top:33px">Phone: +39-3470552814</span>
    <svg class="abs" style="left:481px;top:67px" width="18" height="13" viewBox="0 0 18 13"><rect x="0.5" y="0.5" width="17" height="12" fill="#e8e8e8" stroke="#999"/><polyline points="1,1 9,7 17,1" fill="none" stroke="#888"/></svg>
    <span class="abs footer-line" style="left:509px;top:64px">Email: info@pruettmillwork.com</span>
    <svg class="abs" style="left:483px;top:94px" width="16" height="20" viewBox="0 0 16 20"><path d="M8 19C8 19 1 11 1 7A7 7 0 0 1 15 7C15 11 8 19 8 19Z" fill="#d99a3a" stroke="#fff" stroke-width="1"/><circle cx="8" cy="7" r="2.5" fill="#fff"/></svg>
    <span class="abs footer-line" style="left:509px;top:96px">Address Via Lunetta 42</span>
    <span class="abs footer-line" style="left:509px;top:127px">Cxxx22 (RC) Borgo di Calverno</span>
    <span class="abs" style="left:484px;top:151px;width:16px;height:16px;border-radius:3px;background:#4aa3d8"></span>
    <span class="abs footer-line" style="left:514px;top:150px">pruett_works</span>

    <div class="abs col-divider" style="left:768px;top:14px;height:166px;background:#777"></div>
    <div class="abs tweet-box">
      <span class="abs" style="left:13px;top:8px;width:34px;height:40px;border-radius:4px;background:linear-gradient(#b86a2a,#d89a4a 45%,#6ea5c9)" role="img" aria-label="Follow badge"></span>
      <span class="abs footer-line" style="left:61px;top:23px">@pruett</span>
      <p class="abs tweet-text" style="left:12px;top:58px">Latest Tweet<br>New Inspiration for<br>Design<br>lorem Ipsum<br>Wiew Design</p>
    </div>
    <span class="abs social" style="left:985px;top:16px;background:#2f78b8"></span>
    <span class="abs social" style="left:985px;top:54px;background:#5b86c8"></span>
    <span class="abs social" style="left:985px;top:95px;background:#f2f2f2"></span>
    <span class="abs social" style="left:985px;top:130px;background:#f2f2f2"></span>
  </footer>

  <div class="abs copyright">Copyright 2014 Pruett Design &amp; Millwork</div>
</div>
</body>
</html>
```